Family Ranch with a hobby vineyard needs 2 wine labels for our first harvest

Design 2 wine labels (front and back) with the Brindor Ranch logo.
Label 1:
Sauvignon Blanc
Alc. 12.5% by Vol.
Palos Verdes Peninsula - add as the region
Year 2022
Label 2:
Cabernet Sauvignon
Alc. 13.5% by Vol.
Year 2022
For the back label design:
GOVERNMENT WARNING: (1) According to the Surgeon General, women
should not drink alcoholic beverages during pregnancy because of the risk of
birth defects. (2) Consumption of alcoholic beverages impairs your ability to
drive a car or operate machinery, and may cause health problems.
Contains Sulfates.
750ML
I just received the bottles and have attached a picture.
Look and feel
Each slider illustrates characteristics of the customer's brand and the style your logo design should communicate.

```html
<!DOCTYPE html>
<html lang="en">
<head>
<meta charset="utf-8">
<title>Brindor Ranch – Cabernet Sauvignon 2022 Label</title>
<link href="https://fonts.googleapis.com/css2?family=Montserrat:wght@500&family=Cormorant+Garamond:ital,wght@0,500;1,600&display=swap" rel="stylesheet">
<style>
  :root {
    --backdrop: #0c0c0c;
    --label-paper: #f3f3f3;
    --label-edge: #e4e4e4;
    --ink-dark: #1f1f1f;
    --ink-grey: #3a3a3a;
    --wine-red: #8a1c1c;
    --art-light: #e2e2e2;
    --art-mid: #a9a9a9;
  }
  * { margin: 0; padding: 0; box-sizing: border-box; }
  html, body {
    width: 1200px;
    height: 771px;
    overflow: hidden;
    background: var(--backdrop);
  }
  .canvas {
    position: relative;
    width: 1200px;
    height: 771px;
    background: var(--backdrop);
  }
  .front-label {
    position: absolute;
    left: 349px;
    top: 55px;
    width: 502px;
    height: 660px;
    background: linear-gradient(90deg, var(--label-edge) 0%, var(--label-paper) 12%, var(--label-paper) 88%, var(--label-edge) 100%);
    overflow: hidden;
  }
  .brand-name {
    position: absolute;
    top: 175px;
    left: 0;
    width: 100%;
    text-align: center;
    font-family: "Montserrat", sans-serif;
    font-weight: 500;
    font-size: 38px;
    letter-spacing: 1px;
    color: var(--ink-dark);
  }
  .horse-artwork {
    position: absolute;
    left: 0;
    top: 255px;
    width: 260px;
    height: 405px;
    background: radial-gradient(ellipse at 55% 50%, var(--art-mid) 0%, var(--art-light) 55%, rgba(243,243,243,0) 80%);
  }
  .wine-details {
    position: absolute;
    left: 220px;
    width: 265px;
    text-align: center;
  }
  .varietal {
    top: 402px;
    font-family: "Cormorant Garamond", serif;
    font-style: italic;
    font-weight: 600;
    font-size: 29px;
    color: var(--wine-red);
  }
  .vintage {
    top: 448px;
    font-family: "Cormorant Garamond", serif;
    font-weight: 500;
    font-size: 27px;
    letter-spacing: 2px;
    color: var(--ink-grey);
  }
  .region {
    top: 543px;
    font-family: "Cormorant Garamond", serif;
    font-weight: 500;
    font-size: 13px;
    letter-spacing: 1.5px;
    color: var(--wine-red);
    text-transform: uppercase;
  }
  .alcohol {
    top: 583px;
    font-family: "Cormorant Garamond", serif;
    font-style: italic;
    font-weight: 600;
    font-size: 17px;
    color: var(--ink-grey);
  }
</style>
</head>
<body>
  <main class="canvas">
    <section class="front-label">
      <h1 class="brand-name">Brindor Ranch</h1>
      <div class="horse-artwork" role="img" aria-label="Grey pencil sketch of a horse's head wearing a bridle"></div>
      <p class="wine-details varietal">Cabernet Sauvignon</p>
      <p class="wine-details vintage">2022</p>
      <p class="wine-details region">Palos Verdes Peninsula</p>
      <p class="wine-details alcohol">Alc. 12.5% by Vol.</p>
    </section>
  </main>
</body>
</html>
```